Vostra Capital Web Design

Vostra Capital Limited Shenzhen

This project is a 10 page launch website.
Our client is seeking a contemporary homepage design for a Holdings company. Once we are happy with the homepage design and select designer we will request a secondary page design.

Please see attached company LOGO for an idea of style, it incorporates the traditional Chinese furniture lattice work. The Coral Dune website is one of our clients favorite so we would like to see a similar homepage design to this website.

Use the websites below for reference purpose. The first two are Chinese and the second two are international. We would like to see elements of both but more focus on international design.

http://www.evergrande.com/http://www.orliqueholdings.example/pub/default.aspx http://www.coraldune.example/zh/resort_kelvanoru/
http://www.velde-studio.example
http://img-store-a1.picvault.example/originals/4f/a2/91/4fa291c03b7e55d1a86e20f9c4b713ee.jpg

Company Background
VOSTRA CAPITAL, located in Qianhai, China, is a new real-estate project operator, structuring urban-rural real-estate investment and development, and industrial fund investment. The company also invests in supply chain management and supporting infrastructures. To create new spaces and livable cities Vostra Capital develop win-win strategic partnerships with a number of institutions. Currently cooperating with Marlow East Fenbrook, China urban and rural integrated demonstration.

Target Market(s)

B2B property investment. Target market customers are senior level management/decision makers of large corporations. Focusing geographically on the domestic market first and expanding internationally in 2nd and 3rd years.

Industry/Entity Type

Investment

Requirements
Must have
• Since this is a new company, we would like to the website representing growth and power, E.g. like a growing tree.
Should not have
• Low-level vectors such as curency symbols, American dollar.

```html
<!DOCTYPE html>
<html lang="en">
<head>
<meta charset="utf-8">
<title>Vostra Capital</title>
<link href="https://fonts.googleapis.com/css2?family=Roboto:wght@400;500;700&family=Roboto+Condensed:wght@400;500&family=Cabin:wght@400;600&display=swap" rel="stylesheet">
<style>
:root{
  --header:#262626;
  --body:#3d3d3d;
  --footer:#2c2c2c;
  --bottom:#282828;
  --gold:#c9a14a;
  --gold-soft:#b8913f;
  --white:#ffffff;
  --text:#e8e8e8;
  --muted:#d0d0d0;
  --line:#5a5a5a;
  --blue:#2a8fe2;
}
*{margin:0;padding:0;box-sizing:border-box}
html,body{width:804px;height:1200px;overflow:hidden;background:var(--body)}
body{position:relative;font-family:"Roboto",Arial,sans-serif;color:var(--text)}
.abs{position:absolute}

/* header */
.site-header{left:0;top:0;width:804px;height:115px;background:var(--header)}
.brand-name{left:58px;top:48px;font-family:"Roboto",Arial,sans-serif;font-weight:500;font-size:16px;color:var(--white);letter-spacing:.5px;white-space:nowrap}
.search{left:474px;top:22px;width:174px;height:24px;background:#383838;border:1px solid #474747;font-size:10px;color:#cfcfcf;padding:5px 9px}
.search svg{position:absolute;right:7px;top:6px}
.lang{left:705px;top:28px;font-size:10px;color:var(--white)}
.lang svg{margin-left:8px;vertical-align:1px}
.nav{top:78px;font-size:11.5px;font-weight:700;color:var(--white);letter-spacing:.2px}
.nav.active{color:var(--gold)}
.nav-marker{left:324px;top:111px;width:41px;height:4px;background:var(--gold-soft)}
.nav-marker::before{content:"";position:absolute;left:16px;top:-4px;border:4px solid transparent;border-bottom-color:var(--gold-soft);border-top:0}

/* hero */
.hero{left:0;top:115px;width:804px;height:333px;background:radial-gradient(ellipse at 35% 45%,#e8f6f6 0%,#c5e6e7 45%,#a6d6d9 100%)}
.hero-photo{left:0;top:0;width:804px;height:333px;background:linear-gradient(100deg,rgba(0,0,0,0) 20%,rgba(225,180,150,.35) 45%,rgba(225,180,150,.45) 75%,rgba(0,0,0,0) 95%)}
.hero-caption{left:374px;top:109px;width:371px;height:44px;background:rgba(100,100,100,.85);color:var(--white);font-size:18px;padding:12px 14px;letter-spacing:.2px;white-space:nowrap}
.dots{left:712px;display:flex;gap:2px}
.dots span{width:6px;height:6px;border-radius:50%;background:#333;border:1px solid #333}
.dots span.on{background:#fff}

/* services */
.service{width:210px;text-align:center}
.service-badge{position:relative;margin:0 auto;width:100px;height:100px;border-radius:50%;background:#8e8e8e;box-shadow:0 0 10px rgba(0,0,0,.35)}
.service-badge .face{position:absolute;left:7px;top:7px;width:86px;height:86px;border-radius:50%;background:radial-gradient(circle at 50% 40%,#ffffff,#dedede 70%,#c8c8c8);display:flex;align-items:center;justify-content:center}
.service h3{margin-top:8px;font-family:"Cabin",sans-serif;font-weight:600;font-size:14px;color:var(--gold)}
.service p{margin-top:6px;font-size:9.3px;line-height:16px;color:var(--text)}
.divider{left:84px;top:723px;width:636px;height:1px;background:var(--line)}
.divider::before,.divider::after{content:"";position:absolute;top:-4px;width:9px;height:9px;border-radius:50%;background:#575757}
.divider::before{left:-4px}.divider::after{right:-4px}
.section-title{left:0;width:814px;top:756px;text-align:center;font-family:"Roboto Condensed",sans-serif;font-weight:400;font-size:18.5px;color:var(--white)}

.feature-image{width:153px;height:116px;border:4px solid #8a8a8a}
.feature-image.light{border-color:#ffffff}
.feature-image.mono{background:linear-gradient(180deg,#6a6a6a 0%,#9c9c9c 40%,#4a4a4a 75%,#7a7a7a 100%)}
.feature-image.colour{background:linear-gradient(180deg,#8bb5d6 0%,#b7cde0 35%,#e9dcc0 55%,#cdb998 72%,#566066 100%)}
.feature-text{width:180px}
.feature-text h4{font-weight:400;font-size:10px;color:var(--gold);margin-top:-1px}
.feature-text p{margin-top:6px;font-size:9.2px;line-height:17px;color:var(--text);white-space:nowrap}

/* footer */
.site-footer{left:0;top:970px;width:804px;height:177px;background:var(--footer)}
.footer-col h5{font-size:10.5px;font-weight:500;color:var(--white);letter-spacing:.2px}
.footer-col ul{list-style:none;margin-top:9px}
.footer-col li{font-family:"Cabin",sans-serif;font-size:10px;line-height:19.3px;color:var(--muted)}
.footer-col p{margin-top:8px;font-family:"Cabin",sans-serif;font-size:10px;line-height:19.5px;color:var(--muted)}
.email{left:338px;top:1066px;width:224px;height:23px;background:#fff;border:1px solid #ddd;font-size:9.5px;color:#777;padding:5px 6px}
.subscribe{left:485px;top:1101px;width:77px;height:27px;background:var(--blue);color:#fff;font-family:"Roboto Condensed",sans-serif;font-size:11.5px;text-align:center;line-height:27px}
.social{top:1027px;width:25px;height:25px;display:flex;align-items:center;justify-content:center}
.social.fb{left:619px;background:#3a5aa8}
.social.tw{left:653px;background:#2f9bd8}
.social.feed{left:684px;background:#f06a1e}
.social.video{left:718px;background:#e0282d}
.social span{width:8px;height:8px;border-radius:50%;background:rgba(255,255,255,.85)}
.bottom-bar{left:0;top:1147px;width:804px;height:53px;background:var(--bottom);border-top:1px solid #3a3a3a}
.copyright{left:59px;top:1165px;font-size:9.5px;color:var(--text)}
</style>
</head>
<body>

<header class="abs site-header">
  <div class="abs brand-name">VOSTRA CAPITAL</div>
  <div class="abs search">Search..
    <svg width="9" height="10" viewBox="0 0 9 10"><circle cx="5.5" cy="3.5" r="2.6" fill="none" stroke="#ccc" stroke-width="1.5"/><line x1="3.6" y1="5.4" x2="1" y2="8.5" stroke="#ccc" stroke-width="1.8"/></svg>
  </div>
  <div class="abs lang">ENG<svg width="8" height="6" viewBox="0 0 8 6"><polyline points="1,1 4,4 7,1" fill="none" stroke="#fff" stroke-width="1.8"/></svg></div>
  <nav>
    <div class="abs nav active" style="left:328px">HOME</div>
    <div class="abs nav" style="left:400px">ABOUT US</div>
    <div class="abs nav" style="left:495px">SERVICES</div>
    <div class="abs nav" style="left:589px">PRODUCTS</div>
    <div class="abs nav" style="left:690px">CONTACT</div>
  </nav>
  <div class="abs nav-marker"></div>
</header>

<section class="abs hero">
  <div class="abs hero-photo" role="img" aria-label="Hands holding a phone topped with grass and a young seedling, a finger reaching toward it"></div>
  <div class="abs hero-caption">SUNT IN CULPA QUI OFFICIA DESERUNT</div>
  <div class="abs dots" style="top:315px"><span class="on"></span><span></span><span></span><span></span></div>
</section>

<section>
  <div class="abs service" style="left:75px;top:487px">
    <div class="service-badge"><div class="face">
      <svg width="56" height="34" viewBox="0 0 56 34" fill="#c39a40"><path d="M2 8 L14 4 L24 8 L32 4 L44 6 L54 2 L54 18 L46 20 L34 32 L28 30 L22 32 L14 26 L2 22 Z"/></svg>
    </div></div>
    <h3>Investment</h3>
    <p>Vivamus vel gt magat sagittis.<br>Nulla faucibus nibh a agna tint accumsan<br>hendreritacilisis. Curabitur et libero sit<br>amet ante hendrerit</p>
  </div>
  <div class="abs service" style="left:299px;top:487px">
    <div class="service-badge"><div class="face">
      <svg width="30" height="40" viewBox="0 0 30 40"><rect x="0" y="0" width="30" height="40" rx="4" fill="#c39a40"/><rect x="5" y="5" width="20" height="8" fill="#efefef"/><g fill="#efefef"><rect x="5" y="17" width="5" height="4"/><rect x="12.5" y="17" width="5" height="4"/><rect x="20" y="17" width="5" height="4"/><rect x="5" y="24" width="5" height="4"/><rect x="12.5" y="24" width="5" height="4"/><rect x="20" y="24" width="5" height="4"/><rect x="5" y="31" width="5" height="4"/><rect x="12.5" y="31" width="5" height="4"/><rect x="20" y="31" width="5" height="4"/></g></svg>
    </div></div>
    <h3>Planning</h3>
    <p>Vivamus vel gt magat sagittis.<br>Nulla faucibus nibh a agna tint accumsan<br>hendreritacilisis. Curabitur et libero sit<br>amet ante hendrerit</p>
  </div>
  <div class="abs service" style="left:522px;top:487px">
    <div class="service-badge"><div class="face">
      <svg width="44" height="46" viewBox="0 0 44 46" fill="#c39a40"><polygon points="22,2 42,11 22,20 2,11"/><polygon points="2,14 20,23 20,44 2,35"/><polygon points="24,23 42,14 42,35 24,44"/></svg>
    </div></div>
    <h3>Analysis</h3>
    <p>Vivamus vel gt magat sagittis.<br>Nulla faucibus nibh a agna tint accumsan<br>hendreritacilisis. Curabitur et libero sit<br>amet ante hendrerit</p>
  </div>

  <div class="abs divider"></div>
  <h2 class="abs section-title">WE DEVELOP WIN-WIN STRATEGIC PARTNERSHIPS</h2>

  <div class="abs feature-image mono" style="left:59px;top:809px" role="img" aria-label="Black and white photo of a large suburban house"></div>
  <div class="abs feature-text" style="left:223px;top:818px">
    <h4>Donec dictum soinidales ligula vel</h4>
    <p>Lorem ipsum dolor sit amet, conuitetr<br>adipisicing elit, sed do eiusinmodtipor<br>Morbi blandit feiuingiat lobortis. Cuiur<br>vel massa ac felis tempus pulvinar id<br>ante. Aliquam et enim mauris.</p>
  </div>
  <div class="abs feature-image light colour" style="left:426px;top:809px" role="img" aria-label="Colour photo of cream townhouses under a blue sky"></div>
  <div class="abs feature-text" style="left:589px;top:818px">
    <h4>Donec dictum soinidales ligula vel</h4>
    <p>Lorem ipsum dolor sit amet, conuitetr<br>adipisicing elit, sed do eiusinmodtipor<br>Morbi blandit feiuingiat lobortis. Cuiur<br>vel massa ac felis tempus pulvinar id<br>ante. Aliquam et enim mauris.</p>
  </div>
</section>

<footer>
  <div class="abs site-footer"></div>
  <div class="abs footer-col" style="left:59px;top:1001px">
    <h5>COMPANY</h5>
    <ul><li>About us</li><li>What we do?</li><li>Forums</li><li>Support</li><li>Blog</li></ul>
  </div>
  <div class="abs footer-col" style="left:198px;top:1000px">
    <h5>ABOUT US</h5>
    <ul><li>Vostra Capital</li><li>Contact Us</li><li>Help</li><li>Privacy Policy</li><li>Terms Of Service</li></ul>
  </div>
  <div class="abs footer-col" style="left:338px;top:1000px;width:230px">
    <h5>NEWSLETTER SIGNUP</h5>
    <p>Stay in touch with us by signing up for our quarterly newsletter!</p>
  </div>
  <div class="abs email">Enter Email Id</div>
  <div class="abs subscribe">SUBSCRIBE</div>
  <div class="abs footer-col" style="left:620px;top:1000px"><h5>FOLLOW US ON</h5></div>
  <div class="abs social fb"><span></span></div>
  <div class="abs social tw"><span></span></div>
  <div class="abs social feed"><span></span></div>
  <div class="abs social video"><span></span></div>
  <div class="abs bottom-bar"></div>
  <div class="abs copyright">Copyright ©2013. All Rights Reserved.</div>
</footer>

</body>
</html>
```